Book cover design for modern bagpipe music book

This music book will be A4 in size and requires a design for the front and back cover. The focus is on creating a modern and eye catching design, breaking away from the stereotypes of what people think of when they think of bagpipes. Think the OPPOSITE of a bagpiper in a full kilt standing on top of a mountain playing Copper Lanterns Rising!

Book title: Rise Hum March Rest

Other front cover text : Music for the bagpipes by Dermot Fairley

Front cover file ideas uploaded

2 pictures of bagpipes attached.

- The real set of bagpipes give an idea of the correct finer details

- The toy bagpipes perhaps have a better shape with the left 'stick' down

Back cover - No real brief. Keen for it not to be a full block single colour though.

Design requires 3mm bleed for print

Open to ideas and suggestions! Thank you!

```html
<!DOCTYPE html>
<html lang="en">
<head>
<meta charset="utf-8">
<title>Rise Hum March Rest — Music for the Bagpipes</title>
<link rel="stylesheet" href="https://fonts.googleapis.com/css2?family=Bebas+Neue&display=swap">
<style>
  :root {
    --ink: #111111;
    --paper: #ffffff;
    --accent: #e2262b;
    --icon-ink: #141414;
    --artwork-dark: #1e1e1e;
    --artwork-mid: #4a4a4a;
  }
  * { margin: 0; padding: 0; box-sizing: border-box; }
  html, body { width: 927px; height: 1200px; overflow: hidden; background: var(--paper); }
  .cover {
    position: relative;
    width: 927px; height: 1200px;
    background: var(--paper);
    font-family: "Bebas Neue", "Oswald", sans-serif;
    color: var(--ink);
  }
  .sr-title { position: absolute; left: -9999px; }

  .author-band { position: absolute; left: 0; top: 0; width: 173px; height: 1200px; }
  .author-band text { font-family: "Bebas Neue", sans-serif; fill: var(--paper); }

  .routine { position: absolute; left: 244px; top: 39px; list-style: none; }
  .routine-step {
    display: flex; align-items: center;
    height: 208px; margin-bottom: 27px;
  }
  .step-icon {
    width: 208px; height: 208px;
    border: 9px solid var(--accent);
    border-radius: 26px;
    background: var(--paper);
    box-shadow: 2px 3px 6px rgba(0,0,0,0.25);
    display: flex; align-items: center; justify-content: center;
    flex-shrink: 0;
  }
  .step-icon svg { width: 150px; height: 150px; }
  .pipes-artwork {
    width: 120px; height: 140px;
    background: linear-gradient(160deg, var(--artwork-mid), var(--artwork-dark));
    border-radius: 12px;
  }
  .step-word {
    margin-left: 76px;
    font-size: 168px;
    line-height: 1;
    padding-top: 18px;
    letter-spacing: 1px;
  }

  .tagline { position: absolute; left: 0; top: 0; width: 927px; height: 1200px; pointer-events: none; }
  .tagline text { font-family: "Bebas Neue", sans-serif; }
  .tagline .subtitle { fill: var(--ink); }
  .tagline .instrument { fill: var(--accent); }
</style>
</head>
<body>
<main class="cover">
  <svg class="author-band" viewBox="0 0 173 1200" aria-label="By Dermot Fairley">
    <rect width="173" height="1200" fill="#111111"/>
    <text transform="translate(160,1052) rotate(-90)" font-size="200" textLength="1030" lengthAdjust="spacingAndGlyphs">DERMOT FAIRLEY</text>
    <text transform="translate(118,1152) rotate(-90)" font-size="74" textLength="66" lengthAdjust="spacingAndGlyphs">BY</text>
  </svg>

  <h1 class="sr-title">Rise Hum March Rest</h1>

  <ul class="routine">
    <li class="routine-step">
      <div class="step-icon">
        <svg viewBox="0 0 100 100" aria-hidden="true" fill="var(--icon-ink)">
          <g class="knife" transform="rotate(-42 50 50)">
            <path d="M47 6 C57 14 58 38 54 56 L54 94 a4 4 0 0 1 -8 0 L46 56 Z"/>
          </g>
          <g class="fork" transform="rotate(42 50 50)">
            <rect x="39" y="6" width="3.5" height="24"/>
            <rect x="45" y="6" width="3.5" height="24"/>
            <rect x="51.5" y="6" width="3.5" height="24"/>
            <rect x="57.5" y="6" width="3.5" height="24"/>
            <path d="M39 28 H61 V33 Q61 44 50 46 Q39 44 39 33 Z"/>
            <path d="M46.5 44 H53.5 L54 94 a4 4 0 0 1 -8 0 Z"/>
          </g>
        </svg>
      </div>
      <span class="step-word">RISE</span>
    </li>
    <li class="routine-step">
      <div class="step-icon">
        <svg viewBox="0 0 100 100" aria-hidden="true" fill="var(--icon-ink)">
          <rect x="8" y="28" width="7" height="52"/>
          <rect x="85" y="46" width="7" height="34"/>
          <rect x="8" y="60" width="84" height="10"/>
          <circle cx="27" cy="48" r="8"/>
          <path d="M38 42 h44 a6 6 0 0 1 6 6 v10 h-50 z"/>
        </svg>
      </div>
      <span class="step-word">HUM</span>
    </li>
    <li class="routine-step">
      <div class="step-icon">
        <div class="pipes-artwork" role="img" aria-label="Black bagpipes silhouette illustration"></div>
      </div>
      <span class="step-word">MARCH</span>
    </li>
    <li class="routine-step">
      <div class="step-icon">
        <svg viewBox="0 0 100 100" aria-hidden="true" fill="none" stroke="var(--icon-ink)" stroke-width="9">
          <path d="M20 52 A30 30 0 0 1 72 28"/>
          <path d="M80 48 A30 30 0 0 1 28 72"/>
          <path d="M62 14 L84 22 L72 42 Z" fill="var(--icon-ink)" stroke="none"/>
          <path d="M38 86 L16 78 L28 58 Z" fill="var(--icon-ink)" stroke="none"/>
        </svg>
      </div>
      <span class="step-word">REST</span>
    </li>
  </ul>

  <svg class="tagline" viewBox="0 0 927 1200" aria-label="Music for the bagpipes">
    <text class="subtitle" x="244" y="1038" font-size="72" textLength="420" lengthAdjust="spacingAndGlyphs">MUSIC FOR THE</text>
    <text class="instrument" x="244" y="1151" font-size="134" textLength="629" lengthAdjust="spacingAndGlyphs">BAGPIPES</text>
  </svg>
</main>
</body>
</html>
```